Business Card Design using new attached logo

We are a family run Plumbing and Heating firm looking to improve our company image with an improved business card and new logo.We are looking to keep the company colour (Blue) involved in our design

Reason: New logo added which needs to be incorporated on designs

Industry/Entity Type

Business

Contact Information for Business Card

See attachment of all info required.

Requirements
Must have
• We have just picked a new company logo which is attached.
• Could you please provide your business card designs using this logo.
• We are looking for the logo on the back as well as the front with all the info required

```html
<!DOCTYPE html>
<html lang="en">
<head>
<meta charset="UTF-8">
<title>Brookfield Heating – Business Card</title>
<link rel="stylesheet" href="https://fonts.googleapis.com/css2?family=Lato:wght@400;700&display=swap">
<style>
  :root {
    --brand-blue: #18389a;
    --band-black: #111111;
    --paper-white: #ffffff;
    --ink-black: #111111;
  }
  html, body {
    margin: 0;
    padding: 0;
    overflow: hidden;
    background: var(--brand-blue);
  }
  .card {
    position: relative;
    width: 720px;
    height: 1200px;
    background: var(--brand-blue);
    overflow: hidden;
    font-family: "Lato", sans-serif;
  }
  .brand-band {
    position: absolute;
    left: 0;
    top: 348px;
    width: 100%;
    height: 408px;
    background: var(--band-black);
  }
  .brand-name {
    position: absolute;
    left: 0;
    top: 212px;
    width: 100%;
    margin: 0;
    color: var(--paper-white);
    font-weight: 400;
    font-size: 50px;
    line-height: 1;
    letter-spacing: 2px;
    text-align: center;
    text-transform: uppercase;
  }
  .name-band {
    position: absolute;
    left: 0;
    top: 756px;
    width: 100%;
    height: 113px;
    background: var(--paper-white);
    display: flex;
    flex-direction: column;
    align-items: center;
    justify-content: center;
    color: var(--ink-black);
  }
  .person-name {
    margin: 0;
    font-weight: 700;
    font-size: 48px;
    line-height: 1;
    letter-spacing: 0.5px;
    text-transform: uppercase;
  }
  .person-role {
    margin: 10px 0 0;
    font-weight: 400;
    font-size: 26px;
    line-height: 1;
  }
</style>
</head>
<body>
  <main class="card">
    <section class="brand-band">
      <h1 class="brand-name">Brookfield Heating</h1>
    </section>
    <section class="name-band">
      <p class="person-name">Owen Tasker</p>
      <p class="person-role">Director</p>
    </section>
  </main>
</body>
</html>
```